Informational Website for MOSVALEK-MOSaic VALley Eastern Kinship of Clinic Record Scholars

I need an informational website to help establish us as a legitimate entity. This will help us as we seek funding in to perform the research we intend to carry out. We are a newly formed group of family physicians and primary care researchers from 9 different countries around the world. We have access to electronic medical record data and/or health insurance claims data in our respective countries. We intend to perform international comparative studies in primary care. Our set of projects are to study the impact of the COVID-19 pandemic on primary care in our respective countries and around the world.
I've already purchased a domain and website from Wix. It is a premium account. The domain is https://www.mosvalekclinicnet.org

Target Market(s)

Researchers, policy makers, universities, research funding agencies

Coding

Coded - Design and coding required

Number of Pages Required

5+ page

Font styles to use
Sans Serif

Requirements
Must have
• Must have our logo and an interactive map of the world highlighting Canada, Australia, China (including Hong Kong), Norway, Singapore, South Korea, Sweden, United Kingdom, United States.
This map must be editable such that we can add or remove countries and cities as we evolve. Please see attached brief.
Nice to have
• Nice to depict primary care and big data research

```html
<!DOCTYPE html>
<html lang="en">
<head>
<meta charset="utf-8">
<title>MOSVALEK – Mosaic Valley Eastern Kinship of Clinic Record Scholars</title>
<link href="https://fonts.googleapis.com/css2?family=Montserrat:wght@400;500;600;700&family=Oswald:wght@400&display=swap" rel="stylesheet">
<style>
:root{
  --navy:#0b2d72;
  --navy-deep:#062766;
  --green:#7ea800;
  --sky:#c9dbe5;
  --field:#5f7fae;
  --white:#ffffff;
  --ink:#1c2230;
}
*{margin:0;padding:0;box-sizing:border-box}
html,body{width:1200px;height:2257px;overflow:hidden}
body{position:relative;font-family:"Montserrat",sans-serif;background:var(--white);color:var(--ink)}
.abs{position:absolute}

/* header */
.site-header{position:absolute;left:0;top:0;width:1200px;height:96px;background:var(--white);z-index:3}
.brand-tab{position:absolute;left:88px;top:0;width:212px;height:136px;background:var(--white);border-radius:0 0 106px 106px/0 0 36px 36px;z-index:4;display:flex;flex-direction:column;align-items:center;justify-content:center;gap:8px;padding-top:6px}
.brand-dot{width:44px;height:44px;border-radius:50%;background:var(--navy)}
.brand-name{font-weight:700;font-size:25px;color:var(--navy);letter-spacing:.5px}
.main-nav{position:absolute;top:40px;font-size:12px;font-weight:600;letter-spacing:.8px;color:var(--navy)}
.main-nav.active{color:var(--green)}
.call{position:absolute;left:818px;top:35px;font-family:"Oswald",sans-serif;font-size:18px;color:var(--ink)}
.call span{color:var(--green)}
.btn{position:absolute;display:flex;align-items:center;justify-content:center;font-size:12px;font-weight:700;letter-spacing:.8px;border-radius:3px}
.btn-navy{background:var(--navy);color:var(--white)}
.btn-green{background:var(--green);color:var(--white)}

/* hero */
.hero{position:absolute;left:0;top:96px;width:1200px;height:480px;background:linear-gradient(110deg,#6d6258 0%,#4d5e78 40%,#3a5684 70%,#4d6a95 100%)}
.hero-title{position:absolute;left:0;top:264px;width:1200px;text-align:center;color:var(--white);font-weight:700;font-size:31px;line-height:38px;letter-spacing:.3px}

/* section headings */
.section-heading{position:absolute;left:0;width:1200px;display:flex;justify-content:center;align-items:center;gap:26px;font-weight:600;font-size:29px;color:var(--ink)}
.section-heading::before,.section-heading::after{content:"";width:80px;height:2px;background:var(--green)}
.section-heading.light{color:var(--white)}

/* service cards */
.service-card{position:absolute;top:764px;width:320px;height:311px;color:var(--white);text-align:center;border-radius:2px}
.service-card.navy{background:var(--navy)}
.service-card.green{background:var(--green)}
.service-icon{position:absolute;left:112px;top:-48px;width:96px;height:96px;border-radius:50%;background:var(--white);border:2px solid var(--navy);display:flex;align-items:center;justify-content:center}
.service-card.green .service-icon{border-color:var(--green)}
.service-title{position:absolute;left:0;top:68px;width:100%;font-size:16px;font-weight:600;letter-spacing:.5px}
.service-text{position:absolute;left:26px;top:106px;width:268px;font-size:12.6px;line-height:17.6px}
.service-btn{position:absolute;left:104px;top:239px;width:112px;height:40px;border:1.5px solid var(--white);border-radius:3px;display:flex;align-items:center;justify-content:center;font-size:12px;font-weight:700;letter-spacing:.6px;color:var(--white)}
.service-card.green .service-btn{background:var(--white);color:var(--green)}

/* about */
.about{position:absolute;left:0;top:1155px;width:1200px;height:402px;background:var(--sky)}
.about-lead{position:absolute;left:0;top:130px;width:1200px;text-align:center;font-size:13px;font-weight:600;line-height:19px;color:var(--navy);letter-spacing:.2px}
.about-text{position:absolute;left:150px;top:188px;width:900px;text-align:center;font-size:13.3px;line-height:19px;color:#2a4a86}

/* contact */
.contact{position:absolute;left:0;top:1557px;width:1200px;height:700px;background:var(--navy-deep)}
.org{position:absolute;left:88px;top:134px;color:var(--white);font-weight:600;font-size:15px;letter-spacing:.3px}
.org-detail{position:absolute;left:88px;top:176px;color:var(--white);font-size:12.4px;line-height:19px}
.org-detail b{font-weight:600}
.org-line{position:absolute;left:88px;top:253px;color:var(--white);font-size:12.4px}
.field{position:absolute;background:var(--field);border-radius:2px;color:#eef2f8;font-size:12.4px;padding:12px 14px}
.map{position:absolute;left:616px;top:140px;width:496px;height:416px;background:linear-gradient(135deg,#eeeae2,#e6e2d8 55%,#f0d9d2);border-radius:2px}
.rule{position:absolute;left:88px;top:618px;width:1024px;height:1px;background:#39548c}
.copyright{position:absolute;left:88px;top:649px;color:var(--white);font-size:12.4px}
.copyright span{color:var(--green)}
.social{position:absolute;top:642px;width:31px;height:31px;border-radius:50%;border:1.5px solid var(--green)}
.social.on{background:var(--green)}
</style>
</head>
<body>

<header class="site-header">
  <div class="main-nav active" style="left:399px">HOME</div>
  <div class="main-nav" style="left:479px">ABOUT US</div>
  <div class="main-nav" style="left:588px">SERVICES</div>
  <div class="main-nav" style="left:693px">CONTACT US</div>
  <div class="call"><span>Call:</span> +123 45 60218</div>
  <div class="btn btn-navy" style="left:984px;top:28px;width:128px;height:39px">GET IN TOUCH</div>
</header>
<div class="brand-tab">
  <div class="brand-dot"></div>
  <div class="brand-name">MOSVALEK</div>
</div>

<section class="hero" role="img" aria-label="Photo of a doctor's hands writing on a desk with a stethoscope, overlaid with faint medical data graphics">
</section>
<h1 class="hero-title">INTERNATIONAL CONSORTIUM OF PRIMARY CARE<br>CLINIC RECORD SCHOLARS</h1>
<div class="btn btn-green" style="left:536px;top:364px;width:127px;height:39px">CONTACT US</div>

<h2 class="section-heading" style="top:646px">SERVICES WE PROVIDE</h2>

<article class="service-card navy" style="left:88px">
  <div class="service-icon">
    <svg width="50" height="44" viewBox="0 0 50 44" fill="none" stroke="#0b2d72" stroke-width="2.2" stroke-linejoin="round" stroke-linecap="round">
      <path d="M24 40 C10 30 3 22 3 13 A10 10 0 0 1 24 9 A10 10 0 0 1 45 13"/>
      <path d="M4 22 H14 L18 15 L22 28 L26 22 H30"/>
      <circle cx="39" cy="26" r="8"/><path d="M39 22 V30 M35 26 H43"/>
    </svg>
  </div>
  <h3 class="service-title">PRIMARY CARE</h3>
  <p class="service-text">It is a long established fact that a reader will be distracted by the readable content of a page when looking at its layout. The point of using Lorem Ipsum is that it has a more-or-less normal distribution of letters, as opposed ...</p>
  <div class="service-btn">READ MORE</div>
</article>

<article class="service-card green" style="left:440px">
  <div class="service-icon">
    <svg width="48" height="48" viewBox="0 0 48 48" fill="none" stroke="#0b2d72" stroke-width="2" stroke-linejoin="round" stroke-linecap="round">
      <rect x="8" y="8" width="26" height="34" rx="2"/>
      <path d="M13 30 L19 23 L24 27 L32 16 M28 16 H32 V20"/>
      <path d="M13 36 H24"/>
      <circle cx="36" cy="34" r="7"/><path d="M36 27 V34 H43"/>
    </svg>
  </div>
  <h3 class="service-title">BIG DATA RESEARCH</h3>
  <p class="service-text">It is a long established fact that a reader will be distracted by the readable content of a page when looking at its layout. The point of using Lorem Ipsum is that it has a more-or-less normal distribution of letters, as opposed ...</p>
  <div class="service-btn">READ MORE</div>
</article>

<article class="service-card navy" style="left:792px">
  <div class="service-icon">
    <svg width="48" height="48" viewBox="0 0 48 48" fill="none" stroke="#0b2d72" stroke-width="2.2">
      <circle cx="24" cy="24" r="20"/>
      <ellipse cx="24" cy="24" rx="9" ry="20"/>
      <path d="M4 24 H44 M8 13 H40 M8 35 H40"/>
    </svg>
  </div>
  <h3 class="service-title">INTERNATIONAL</h3>
  <p class="service-text">It is a long established fact that a reader will be distracted by the readable content of a page when looking at its layout. The point of using Lorem Ipsum is that it has a more-or-less normal distribution of letters, as opposed ...</p>
  <div class="service-btn">READ MORE</div>
</article>

<section class="about">
  <h2 class="section-heading" style="top:72px">ABOUT US</h2>
  <p class="about-lead">WE ARE A GROUP OF FAMILY PHYSICIANS AND PRIMARY CARE HEALTH SERVICES RESEARCHERS COLLABORATING TOGETHER<br>TO STUDY THE IMPACT OF THE COVID-19 &nbsp;PANDEMIC ON PRIMARY CARE AROUND THE WORLD.</p>
  <p class="about-text">Lorem Ipsum is simply dummy text of the printing and typesetting industry. Lorem Ipsum has been the industry's standard dummy text ever since the 1500s, when an unknown printer took a galley of type and scrambled it to make a type specimen book. has survived not only five centuries, but also the leap into electronic typesetting, remaining essentially unchanged. It was popularised in the 1960s with the release of Letraset sheets containing</p>
  <div class="btn btn-navy" style="left:528px;top:290px;width:144px;height:40px">DISCOVER MORE</div>
</section>

<section class="contact">
  <h2 class="section-heading light" style="top:72px">CONTACT US</h2>
  <div class="org">MOSVALEK</div>
  <div class="org-detail"><b>Department of Community Clinic Studies</b><br><b>Mosaic Valley Institute of Health</b><br>48 Larchmere Road, 3rd Floor, Eastvale, EV4 2QT</div>
  <div class="org-line">Call Us: +123-456-0418 &nbsp;&nbsp;&nbsp;&nbsp;I&nbsp;&nbsp;&nbsp;&nbsp; Email: r.hale@mosvalekclinicnet.org</div>

  <div class="field" style="left:88px;top:306px;width:240px;height:39px">Name</div>
  <div class="field" style="left:344px;top:306px;width:239px;height:39px">Phone</div>
  <div class="field" style="left:88px;top:361px;width:240px;height:40px">Email</div>
  <div class="field" style="left:344px;top:361px;width:239px;height:40px">Subject</div>
  <div class="field" style="left:88px;top:418px;width:495px;height:79px">Message</div>
  <div class="btn btn-green" style="left:88px;top:514px;width:128px;height:39px">SUBMIT</div>

  <div class="map" role="img" aria-label="Street map around the consortium's office with a location pin and address label"></div>

  <div class="rule"></div>
  <div class="copyright">© 2021 <span>MOSVALEK</span>. All Rights Reseved</div>
  <div class="social" style="left:617px"></div>
  <div class="social on" style="left:656px"></div>
  <div class="social" style="left:695px"></div>
  <svg class="abs" style="left:1094px;top:646px" width="18" height="22" viewBox="0 0 18 22" fill="none" stroke="#7ea800" stroke-width="2" stroke-linejoin="round">
    <path d="M9 2 L16 20 L9 15 L2 20 Z"/>
  </svg>
</section>

</body>
</html>
```